Business Card Design Project

We are looking for a new business card design for a Drilling company in WA, Australia.

We are in between offices, however require a design in the meantime due to some upcoming events with our basic information.

The Logo for our company is Blue and Grey and would like this colour scheme throughout.

We are quite a new company so would like a memorable design that stands out and communicates a strong commitment to safety, quality of work and performance.

The company name is Ridgeback Boring Works (RBW)

The details to be included are as follows:

Martin Calloway
Managing Director
m.0481639027
e.martin@rbwgroup.com.au

Simon Calloway
Director
m.0429561384
e.simon@rbwgroup.com.au

Industry/Entity Type

Events

Requirements
Must have
• Under the Logo, we would like 'Western Australia'

```html
<!DOCTYPE html>
<html lang="en">
<head>
<meta charset="utf-8">
<title>Ridgeback Boring Works – Business Cards</title>
<link rel="stylesheet" href="https://fonts.googleapis.com/css2?family=PT+Sans:wght@400;700&family=PT+Sans+Narrow:wght@700&display=swap">
<style>
  :root {
    --page: #ffffff;
    --card-ground: #f1f2f4;
    --card-ground-soft: #e6e8eb;
    --brand-blue: #1d3f8f;
    --brand-grey: #7d8085;
    --ink: #222326;
    --band-dark: #0d2a66;
    --band-mid: #1656b4;
    --band-light: #2f86d8;
  }
  * { box-sizing: border-box; margin: 0; padding: 0; }
  html, body {
    width: 1200px; height: 900px; overflow: hidden;
    background: var(--page);
    font-family: "PT Sans", Arial, sans-serif;
  }
  .sheet {
    width: 1200px; height: 900px;
    display: flex; justify-content: center; align-items: center; gap: 90px;
  }
  .card {
    position: relative;
    width: 340px; height: 556px;
    background: var(--card-ground);
    box-shadow: 0 2px 10px rgba(0,0,0,0.12);
    overflow: hidden;
  }
  .card__texture {
    position: absolute; inset: 0 0 116px 0;
    background: radial-gradient(circle at 50% 40%, var(--card-ground) 0%, var(--card-ground-soft) 100%);
  }
  .card__brand {
    position: absolute; top: 62px; left: 0; right: 0;
    display: flex; flex-direction: column; align-items: center; gap: 8px;
  }
  .brand__lockup {
    display: flex; align-items: center; gap: 10px;
  }
  .card__brand-mark {
    width: 14px; height: 14px; background: var(--brand-blue);
  }
  .card__brand-name {
    font-family: "PT Sans Narrow", "PT Sans", sans-serif;
    font-weight: 700; font-size: 30px; line-height: 1.05;
    color: var(--brand-blue); text-transform: uppercase;
    text-align: left;
  }
  .card__region {
    font-size: 12px; letter-spacing: 0.22em; text-transform: uppercase;
    color: var(--brand-grey); padding-left: 24px;
  }
  .card__contact {
    position: absolute; top: 232px; left: 0; right: 0;
    text-align: center;
  }
  .contact__name {
    font-weight: 700; font-size: 22px; color: var(--brand-blue);
  }
  .contact__role {
    font-size: 12px; color: var(--ink); margin-top: 2px;
  }
  .contact__mobile {
    font-size: 17px; color: var(--band-mid); margin-top: 18px;
  }
  .contact__email {
    font-size: 17px; color: var(--ink); margin-top: 22px;
  }
  .card__band {
    position: absolute; left: 0; right: 0; bottom: 0; height: 116px;
    background:
      repeating-linear-gradient(180deg, rgba(255,255,255,0.10) 0 1px, transparent 1px 3px, rgba(0,0,0,0.14) 3px 4px, transparent 4px 6px),
      linear-gradient(180deg, var(--band-light) 0%, var(--band-mid) 45%, var(--band-dark) 100%);
  }
  .card__band-edge {
    position: absolute; left: 0; right: 0; bottom: 0; height: 18px;
    background: var(--band-dark);
  }
</style>
</head>
<body>
<main class="sheet">

  <article class="card">
    <div class="card__texture" role="img" aria-label="Soft grey damask-style background pattern"></div>
    <header class="card__brand">
      <div class="brand__lockup">
        <span class="card__brand-mark"></span>
        <span class="card__brand-name">Ridgeback<br>Boring Works</span>
      </div>
      <p class="card__region">Western Australia</p>
    </header>
    <section class="card__contact">
      <p class="contact__name">Martin Calloway</p>
      <p class="contact__role">Managing Director</p>
      <p class="contact__mobile">M. 0481639027</p>
      <p class="contact__email">E. martin@rbwgroup.com.au</p>
    </section>
    <div class="card__band"><div class="card__band-edge"></div></div>
  </article>

  <article class="card">
    <div class="card__texture" role="img" aria-label="Soft grey damask-style background pattern"></div>
    <header class="card__brand">
      <div class="brand__lockup">
        <span class="card__brand-mark"></span>
        <span class="card__brand-name">Ridgeback<br>Boring Works</span>
      </div>
      <p class="card__region">Western Australia</p>
    </header>
    <section class="card__contact">
      <p class="contact__name">Simon Calloway</p>
      <p class="contact__role">Director</p>
      <p class="contact__mobile">M. 0429561384</p>
      <p class="contact__email">E. simon@rbwgroup.com.au</p>
    </section>
    <div class="card__band"><div class="card__band-edge"></div></div>
  </article>

</main>
</body>
</html>
```